Email footer project

We are looking for a standardised email footer that can be changed monthly for various project we are working on.
Please refer to EMAIL FOOTER BRIEF FOR ALL INFORMATION

We have uploaded some previous footers as a sample.

Target Market(s)

property, environmental

Industry/Entity Type

energy and property

Colors
00AB8E
00BBA5
67D7C9
C6EFE9
E9F9F6

Requirements
Must have
• company branding - verdalith.co.uk.

```html
<!DOCTYPE html>
<html lang="en">
<head>
<meta charset="utf-8">
<title>Delivering Net Zero – Webinar Series</title>
<link rel="stylesheet" href="https://fonts.googleapis.com/css2?family=Roboto+Condensed:wght@300;400;700&display=swap">
<style>
  :root {
    --ink: #3b3b3b;
    --green: #2fb34a;
    --olive: #5a9e21;
    --brace: #b9cbd3;
    --panel: #10230f;
    --slate: #3c4b53;
    --leaf: #3aa935;
    --lime: #8cc63f;
    --sun: #f7e02a;
    --sun-deep: #f0c800;
    --skin: #8a5a3c;
    --alert: #f15a24;
    --white: #ffffff;
    --mist: #ececec;
  }
  html, body { margin: 0; padding: 0; overflow: hidden; background: var(--white); }
  .banner {
    position: relative;
    width: 1200px;
    height: 240px;
    overflow: hidden;
    background: var(--white);
    font-family: "Roboto Condensed", "Arial Narrow", sans-serif;
    font-weight: 700;
  }
  .backdrop { position: absolute; inset: 0; width: 1200px; height: 240px; }
  .line { position: absolute; margin: 0; line-height: 1; white-space: nowrap; text-transform: uppercase; }
  .title-lead { left: 34px; top: 58px; font-size: 42px; letter-spacing: 3px; color: var(--ink); }
  .title-main { left: 32px; top: 108px; font-size: 73px; letter-spacing: 1px; color: var(--green); }
  .hand {
    position: absolute; left: 296px; top: 178px; width: 40px; height: 62px;
    border-radius: 14px 14px 4px 4px;
    background: linear-gradient(180deg, var(--skin), #6e4329);
  }
  .hero-o {
    left: 300px; top: 41px; font-size: 185px;
    color: var(--sun);
    background: linear-gradient(160deg, var(--sun), var(--sun-deep));
    -webkit-background-clip: text; background-clip: text;
    -webkit-text-fill-color: transparent;
  }
  .series-a { left: 440px; top: 88px; font-size: 26px; letter-spacing: 3px; color: var(--olive); }
  .series-b { left: 440px; top: 118px; font-size: 40px; letter-spacing: 1px; color: var(--olive); }
  .brace { position: absolute; left: 564px; top: 48px; width: 40px; height: 150px; }
  .topic { left: 628px; font-size: 58px; }
  .topic-1 { top: 28px; color: var(--ink); }
  .topic-2 { top: 88px; color: var(--green); }
  .topic-3 { top: 148px; color: var(--green); }
  .amp { font-weight: 300; color: var(--ink); }
  .cta { left: 936px; width: 220px; text-align: center; color: var(--white); }
  .cta-1 { top: 40px; font-size: 44px; }
  .cta-2 { top: 84px; font-size: 52px; }
  .pointer { position: absolute; left: 1014px; top: 140px; width: 70px; height: 80px; }
  .brand {
    position: absolute; left: 34px; top: 212px; margin: 0;
    font-size: 16px; font-weight: 700; letter-spacing: 1px; line-height: 1;
    color: var(--ink);
  }
</style>
</head>
<body>
<main class="banner">
  <svg class="backdrop" viewBox="0 0 1000 200" preserveAspectRatio="none" aria-hidden="true">
    <defs>
      <linearGradient id="haze" x1="0" y1="0" x2="1" y2="0">
        <stop offset="0" stop-color="#ffffff"/>
        <stop offset="1" stop-color="#e6e6e6"/>
      </linearGradient>
    </defs>
    <polygon points="300,0 620,0 760,200 430,200" fill="url(#haze)" opacity="0.7"/>
    <polygon points="560,0 700,0 800,200 640,200" fill="var(--mist)" opacity="0.6"/>
    <polygon points="700,0 860,0 790,100 640,100" fill="var(--slate)"/>
    <polygon points="680,200 760,120 800,120 780,200" fill="var(--lime)"/>
    <polygon points="700,200 790,100 850,100 850,200" fill="var(--leaf)"/>
    <polygon points="840,0 1000,0 1000,200 840,200 772,100" fill="var(--panel)"/>
  </svg>

  <h1 class="line title-lead">Delivering</h1>
  <p class="line title-main">Net Zer</p>
  <div class="hand" role="img" aria-label="Hand raising the letter O from below"></div>
  <p class="line hero-o" aria-label="O">O</p>

  <p class="line series-a">Webinar</p>
  <p class="line series-b">Series</p>

  <svg class="brace" viewBox="0 0 40 150" aria-hidden="true">
    <path d="M6 4 C22 4 20 22 20 44 C20 62 22 73 34 75 C22 77 20 88 20 106 C20 128 22 146 6 146"
          fill="none" stroke="var(--brace)" stroke-width="5" stroke-linecap="round"/>
  </svg>

  <p class="line topic topic-1">MEES,</p>
  <p class="line topic topic-2">EPCS</p>
  <p class="line topic topic-3"><span class="amp">&amp;</span> ESG</p>

  <p class="line cta cta-1">Register</p>
  <p class="line cta cta-2">Online</p>

  <svg class="pointer" viewBox="0 0 70 80" aria-hidden="true">
    <circle cx="30" cy="26" r="18" fill="none" stroke="var(--alert)" stroke-width="3"/>
    <circle cx="30" cy="26" r="10" fill="var(--alert)"/>
    <path d="M25 26 a5 5 0 0 1 10 0 v20 h4 a4 4 0 0 1 8 2 a4 4 0 0 1 8 2 a4 4 0 0 1 8 3 v12 c0 8 -6 14 -14 14 h-12 c-6 0 -10 -4 -13 -9 l-9 -14 a4 4 0 0 1 7 -5 l3 4 z"
          fill="var(--white)" stroke="#9aa3a8" stroke-width="1.6" stroke-linejoin="round"/>
  </svg>

  <p class="brand">verdalith.co.uk</p>
</main>
</body>
</html>
```